731 Orchard Avenue Residences

designing a sign for apartment complex;
prefer colors gray white and yellow

Target Market(s)

residents coming home to their apartment

Font styles to use
Serif
Sans Serif

Colors
FFF300
FFF600
FEFA6F
FFFEC7
FFFEE8

Requirements
Must have
• black or gray, white and some yellow; easy to read and see

```html
<!DOCTYPE html>
<html lang="en">
<head>
<meta charset="utf-8">
<title>731 Orchard Avenue Residences – Entrance Sign</title>
<link rel="stylesheet" href="https://fonts.googleapis.com/css2?family=Playfair+Display:wght@700;900&display=swap">
<style>
  :root {
    --backdrop: #000000;
    --sign-white: #ffffff;
    --sign-gray: #999999;
    --ring-gray: #6b6b6b;
    --accent-yellow: #fff300;
    --swoosh-yellow: #ffd900;
    --ink: #111111;
    --subtitle-gray: #9a9a9a;
  }
  html, body {
    margin: 0;
    width: 1200px;
    height: 1000px;
    overflow: hidden;
    background: var(--backdrop);
  }
  .canvas {
    width: 1200px;
    height: 1000px;
    display: flex;
    align-items: center;
    justify-content: center;
  }
  .entrance-sign {
    width: 1000px;
    height: 540px;
    display: block;
  }
  .panel-back { fill: var(--sign-gray); }
  .swoosh-top, .swoosh-edge { fill: var(--swoosh-yellow); }
  .panel-front { fill: var(--sign-white); }
  .base-band { fill: var(--accent-yellow); }
  .brand-dot { fill: var(--accent-yellow); stroke: var(--ring-gray); stroke-width: 5; }
  .sign-name {
    font-family: "Playfair Display", Georgia, serif;
    font-weight: 900;
    font-size: 41px;
    fill: var(--ink);
  }
  .sign-subtitle {
    font-family: "Playfair Display", Georgia, serif;
    font-weight: 700;
    font-size: 27px;
    fill: var(--subtitle-gray);
  }
  .rule { stroke: var(--ink); stroke-width: 2; }
</style>
</head>
<body>
<main class="canvas">
  <svg class="entrance-sign" viewBox="0 0 740 400" role="img" aria-label="731 Orchard Avenue Residences entrance sign">
    <!-- rear gray panel -->
    <polygon class="panel-back" points="24,4 712,16 709,226 24,226"/>
    <!-- thin yellow swoosh along the top edge -->
    <path class="swoosh-top" d="M24,4 C160,28 360,28 500,12 Z"/>
    <!-- yellow edge sweeping along the front panel -->
    <path class="swoosh-edge" d="M4,48 C260,46 520,100 706,216 L708,224 C520,112 260,54 4,50 Z"/>
    <!-- white front panel -->
    <path class="panel-front" d="M4,50 C260,54 520,112 708,224 L736,242 L736,364 L4,364 Z"/>
    <!-- yellow base band -->
    <rect class="base-band" x="27" y="364" width="679" height="30"/>

    <!-- brand mark -->
    <circle class="brand-dot" cx="374" cy="178" r="32"/>

    <text class="sign-name" x="374" y="292" text-anchor="middle">731 Orchard Avenue</text>
    <line class="rule" x1="177" y1="318" x2="268" y2="318"/>
    <text class="sign-subtitle" x="374" y="327" text-anchor="middle">residences</text>
    <line class="rule" x1="480" y1="318" x2="573" y2="318"/>
  </svg>
</main>
</body>
</html>
```